Brightline Balance Systems Tri Page Flyer

Hi, I am after a try fold flyer to promote my new business. My Business Brightline Balance Systems is a sales and service based weighing equipment business based around both scales and service. I really want to see ad ensign that grabs attention as this will be my primary drop off brochure on cold calls and mail outs as an introductory flee for my business.I want background pics of industries from Food, logistics, Medical ( as per my sample brochure states) with colours and appeal to entice customers to read not just receive and dispose!From my logo that involves green i would like to roll around that them with greys and blues.Feel free to alter my wording from my sample. i will offer some more Hi Res pics but want to get started. I think with a tri open brochure the product literature and pics can be located on each side and details through the centre page.i also feel if you can headline the wording in sections that would attract a better audience.I look forward to your exciting designs. Please let me know asap what pictures are not of a high quality so i can obtain clear Hi Res Jpegs.thanksMarcus Delaney

PLEASE ADD THE FOLLOWING PRODUCT ITEMS TO MY LIST (LISTED ON SECOND PAGE OF BBSPRODUCTS FINAL4.DOC)
AUTOMATED DRUM FILLING EQUIPMENT TO SUIT ALL APPLICATIONS ( PICS APDF 3,6,8,12)
NEW PICS ATTACHED FOR MEDICAL SCALES.
THANKS
ALSO ATTACHED MY LOGO IN A PDF TO USE
PLEASE ADD MY WEBSITE NAME, WWW.bbsystems.com.au
Please also try to utilise the green Tick correct symbol in my logo in the flyer as a symbol of CORRECT.
Thankyou
MARCUS

Target Market(s)

Food manufacturing, medical, logistics, Industrial, retail Applications

Industry/Entity Type

Business

Colors
919191
9d9d9d
00a990
33a6d7

Requirements
Must have
• Appeal for potential customers to read!
• Wording to appeal to readers
Nice to have
• Colours to match my logo, greens, greys, blues
• Background images of manufacturing Industires.
• I would like to emphasise in 1 line that high quality customer service is what I am about, not calling a number put on hold put through to a department that does not answer leaving messages etc etc you are not a number with me!!

```html
<!DOCTYPE html>
<html lang="en">
<head>
<meta charset="utf-8">
<title>Brightline Balance Systems – Products Flyer</title>
<link rel="stylesheet" href="https://fonts.googleapis.com/css2?family=Open+Sans:wght@400;600;700;800&display=swap">
<style>
  :root {
    --canvas: #dcdcdc;
    --sheet: #ffffff;
    --green: #8cc63f;
    --green-dark: #5a9a1e;
    --ink: #2b2b2b;
    --grey: #919191;
    --box: #6d6d6d;
    --orange: #f7931e;
    --tick-red: #d9262c;
    --photo-a: #c9ccd0;
    --photo-b: #e9ebee;
  }
  * { box-sizing: border-box; margin: 0; padding: 0; }
  html, body { width: 876px; height: 1200px; overflow: hidden; }
  body { background: var(--canvas); font-family: "Open Sans", Arial, sans-serif; color: var(--ink); position: relative; }
  .sheet { position: absolute; left: 22px; top: 18px; width: 832px; height: 1164px; background: var(--sheet); box-shadow: 0 2px 8px rgba(0,0,0,.25); }
  .gallery { position: absolute; left: 0; top: 0; width: 330px; height: 860px; }
  .photo { position: absolute; background: linear-gradient(160deg, var(--photo-b), var(--photo-a)); border: 3px solid var(--green); }
  .photo.plain { border-color: transparent; }
  .products { position: absolute; left: 368px; top: 38px; width: 430px; }
  .products h1 { font-size: 34px; font-weight: 800; letter-spacing: .5px; margin-bottom: 14px; }
  .product-list { list-style: none; }
  .product-list li { position: relative; padding-left: 34px; font-size: 19px; line-height: 24px; font-weight: 600; margin-bottom: 4px; }
  .product-list li::before { content: ""; position: absolute; left: 2px; top: 4px; width: 15px; height: 15px; border: 1.5px solid var(--box); }
  .product-list li.checked svg { position: absolute; left: 1px; top: 1px; }
  .green-rule { position: absolute; left: 342px; top: 30px; width: 4px; height: 830px; background: var(--green); }
  .callout { position: absolute; left: 36px; top: 896px; width: 760px; height: 96px; background: var(--orange); color: #fff; font-weight: 700; font-size: 29px; line-height: 36px; text-align: center; display: flex; align-items: center; justify-content: center; }
  .footer { position: absolute; left: 36px; top: 1020px; width: 760px; height: 110px; display: flex; }
  .services { width: 400px; display: grid; grid-template-columns: repeat(3, auto); row-gap: 22px; column-gap: 18px; align-content: center; border-right: 2px solid var(--grey); padding-right: 20px; }
  .service { display: flex; align-items: center; gap: 10px; font-size: 20px; font-weight: 600; }
  .contact { padding-left: 26px; display: flex; flex-direction: column; justify-content: center; gap: 22px; font-size: 19px; font-weight: 600; }
</style>
</head>
<body>
<div class="sheet">
  <div class="gallery">
    <div class="photo plain" style="left:18px;top:30px;width:112px;height:88px" role="img" aria-label="Bench counting scale"></div>
    <div class="photo" style="left:160px;top:28px;width:80px;height:280px" role="img" aria-label="Medical height and weight scale"></div>
    <div class="photo plain" style="left:18px;top:126px;width:112px;height:100px" role="img" aria-label="Retail price computing scale"></div>
    <div class="photo" style="left:14px;top:234px;width:140px;height:176px" role="img" aria-label="Linear weigher filling machine"></div>
    <div class="photo plain" style="left:180px;top:268px;width:140px;height:156px" role="img" aria-label="Pallet jack scale"></div>
    <div class="photo" style="left:14px;top:418px;width:140px;height:190px" role="img" aria-label="Platform scale with indicator"></div>
    <div class="photo plain" style="left:168px;top:436px;width:152px;height:118px" role="img" aria-label="Compact bench scales"></div>
    <div class="photo" style="left:14px;top:616px;width:160px;height:180px" role="img" aria-label="Printer and labeller"></div>
    <div class="photo" style="left:180px;top:620px;width:140px;height:180px" role="img" aria-label="Electronic weighing indicator"></div>
  </div>
  <div class="green-rule"></div>

  <section class="products">
    <h1>PRODUCTS</h1>
    <ul class="product-list">
      <li class="checked"><svg width="20" height="20" viewBox="0 0 20 20"><path d="M3 10 L8 15 L18 3" fill="none" stroke="var(--tick-red)" stroke-width="2.5"/></svg>Electronic Platform Scales Ranging From 30kg-600kg</li>
      <li>Printers and Labellers to suit your requirements</li>
      <li>Linear Weighers to suit all Applications</li>
      <li>Electronic Floor Scales Ranging From 1000kg - 3000kg(Trade Approved)</li>
      <li>Full Range of Electronic and Mechanical Hanging and Crane Scales Ranging from10kg -10Tonne</li>
      <li>Vet Scales ranging from 20kg-300kg</li>
      <li>Electronic Baby Scales</li>
      <li>Pallet Jack Scales to 2000kg</li>
      <li>Full range of TRADE APPROVED SCALES</li>
      <li>Coin and Note Counting Scales</li>
      <li>Shipping/Parcel Scales to suit any application</li>
      <li>High Precision Electronic Balances Ranging From 100-6000g</li>
      <li>Full Range of Electronic Weighing Indicators To suit any application</li>
      <li>Full range of Load Cells and Fittings to suit any Application</li>
      <li>REPAIRS ON ALL WEIGHING AND PACKAGING EQUIPMENT ALL MAKES AND MODELS.</li>
    </ul>
  </section>

  <div class="callout">ASK ABOUT OUR RANGE OF PACKAGING<br>AND FILLING EQUIPMENT</div>

  <footer class="footer">
    <div class="services">
      <span class="service"><svg width="20" height="20" viewBox="0 0 20 20"><rect x="1" y="1" width="18" height="18" fill="none" stroke="var(--box)" stroke-width="1.5"/><path d="M4 10 L8 14 L16 5" fill="none" stroke="var(--green-dark)" stroke-width="2.5"/></svg>Weighing</span>
      <span class="service"><svg width="20" height="20" viewBox="0 0 20 20"><rect x="1" y="1" width="18" height="18" fill="none" stroke="var(--box)" stroke-width="1.5"/><path d="M4 10 L8 14 L16 5" fill="none" stroke="var(--green-dark)" stroke-width="2.5"/></svg>Packaging</span>
      <span class="service"><svg width="20" height="20" viewBox="0 0 20 20"><rect x="1" y="1" width="18" height="18" fill="none" stroke="var(--box)" stroke-width="1.5"/><path d="M4 10 L8 14 L16 5" fill="none" stroke="var(--green-dark)" stroke-width="2.5"/></svg>Filling</span>
      <span class="service"><svg width="20" height="20" viewBox="0 0 20 20"><rect x="1" y="1" width="18" height="18" fill="none" stroke="var(--box)" stroke-width="1.5"/><path d="M4 10 L8 14 L16 5" fill="none" stroke="var(--green-dark)" stroke-width="2.5"/></svg>Sales</span>
      <span class="service"><svg width="20" height="20" viewBox="0 0 20 20"><rect x="1" y="1" width="18" height="18" fill="none" stroke="var(--box)" stroke-width="1.5"/><path d="M4 10 L8 14 L16 5" fill="none" stroke="var(--green-dark)" stroke-width="2.5"/></svg>Services</span>
      <span class="service"><svg width="20" height="20" viewBox="0 0 20 20"><rect x="1" y="1" width="18" height="18" fill="none" stroke="var(--box)" stroke-width="1.5"/><path d="M4 10 L8 14 L16 5" fill="none" stroke="var(--green-dark)" stroke-width="2.5"/></svg>Hire</span>
    </div>
    <div class="contact">
      <span>Contact Marcus: 0400555012</span>
      <span>Email: marcus@bbsystems.com.au</span>
    </div>
  </footer>
</div>
</body>
</html>
```